ORVALIS MED -DIAGNOSTIC CENTRE FOR IMAGES

Our Activity provides diagnostic services for images (RMI, Tac, RX, Ultrasound etc.)
We would like to create a broschure that illustrates our services.
We would like to give maximum attention to the Diagnostic service dedicated to "HEART", therefore maximum evidence to the world of Cardiology.
In the background we would like to highlight the other diagnostic services dedicated to the Rest of the Body (Brain, Knees Legs etc.)
Target Market(s)
PERSONS WHO NEED TO PERFORM DIAGNOSTIC TESTS (MRI, CT, ULTRASOUND, RX ETC.)
Industry/Entity Type
HEALTH
Requirements
Must have
- The company logo, must have diagnostic images (MRI, CT, X-ray, ultrasound), must be simple and intuitive, which is harmonious with the colors of our company logo
Should not have
- Colours that are not in harmony with our company logo

```html
<!DOCTYPE html>
<html lang="en">
<head>
<meta charset="utf-8">
<title>Orvalis Med – Diagnostic Brochure</title>
<link href="https://fonts.googleapis.com/css2?family=Poppins:wght@400;600&family=Montserrat:wght@400;500&display=swap" rel="stylesheet">
<style>
:root{
  --bg:#6f6f6f;
  --paper:#ffffff;
  --blue:#1773c0;
  --blue-soft:#3d8fd2;
  --teal:#1aa79a;
  --ink:#1d1d1f;
}
*{margin:0;padding:0;box-sizing:border-box}
html,body{width:935px;height:1200px;overflow:hidden;background:var(--bg)}
body{position:relative;font-family:"Montserrat",sans-serif;color:var(--ink)}
.spread{position:absolute;left:99px;width:757px;height:534px;background:var(--paper);transform:scale(.974);transform-origin:0 0;box-shadow:0 3px 8px rgba(0,0,0,.35);overflow:hidden}
.spread--cover{top:56px}
.spread--inside{top:619px}
.abs{position:absolute}
.shapes{position:absolute;left:0;top:0;width:757px;height:534px}
.photo{position:absolute}
.photo--doctor{left:0;top:0;width:378px;height:314px;background:linear-gradient(100deg,#dfe8f1 0%,#f4f7fa 30%,#e7edf3 55%,#c8d4e0 80%,#b9c6d3 100%)}
.photo--mri{left:432px;top:302px;width:325px;height:216px;background:linear-gradient(180deg,#dfe5ec 0%,#eef1f4 40%,#c2cfdc 65%,#8fc6ea 85%,#b9d6ea 100%)}
.photo--ct{left:35px;top:85px;width:225px;height:165px;background:radial-gradient(ellipse 60% 55% at 42% 50%,#c9d2db,#e9edf1 60%,rgba(255,255,255,0) 100%)}
.photo--xray{left:619px;top:339px;width:138px;height:180px;background:radial-gradient(ellipse 60% 60% at 55% 60%,#cdd3d9,#eceff2 65%,rgba(255,255,255,0) 100%)}
.contact{left:57px;font-size:11px;display:flex;align-items:center;gap:8px;color:var(--ink)}
.contact svg{width:10px;height:10px}
.web-bar{left:0;top:489px;width:378px;height:25px;background:var(--teal);display:flex;align-items:center;padding-left:56px;gap:10px;color:#fff;font-size:10.5px;letter-spacing:2.5px}
.brand{left:452px;top:66px}
.brand__name{font-family:"Poppins",sans-serif;font-weight:600;font-size:34px;color:var(--blue);line-height:1;display:flex;align-items:center;gap:8px}
.brand__mark{width:14px;height:14px;background:var(--teal);border-radius:50%}
.brand__tag{font-family:"Poppins",sans-serif;font-size:11.5px;color:var(--teal);margin-top:4px;font-weight:400}
.headline{left:402px;top:178px;font-family:"Poppins",sans-serif;font-size:20.5px;line-height:25px;color:var(--blue);font-weight:400}
.headline .accent{font-weight:600;color:var(--teal)}
.headline .strong{font-weight:600}
.info-panel{left:389px;top:0;width:368px;height:194px;background:var(--blue);overflow:hidden}
.info-panel h2{position:absolute;left:18px;top:34px;font-family:"Poppins",sans-serif;font-weight:600;font-size:14.5px;color:#fff;letter-spacing:.3px}
.body-copy{font-size:8.4px;line-height:10.1px;color:#fff}
.info-panel .body-copy{position:absolute;left:18px;top:64px;width:334px;text-align:justify}
.bullets{left:405px;top:208px;font-size:8.4px;line-height:10.1px;list-style:none}
.bullets li{position:relative;padding-left:12px;margin-bottom:6.2px;text-align:justify}
.bullets li::before{content:"";position:absolute;left:0;top:3px;width:4px;height:4px;border-radius:50%;background:var(--ink)}
.bullets .wide{width:322px}
.bullets .narrow{width:192px}
.story-box{left:0;top:298px;width:310px;height:236px;background:var(--blue);overflow:hidden}
.story-box .body-copy{position:absolute;left:27px;top:28px;width:256px}
</style>
</head>
<body>

<section class="spread spread--cover">
  <div class="photo photo--doctor" role="img" aria-label="Cardiologist in a white coat holding a stethoscope, hospital corridor behind"></div>
  <div class="photo photo--mri" role="img" aria-label="Cardiac MRI scanner room with patient table"></div>
  <svg class="shapes" viewBox="0 0 757 534" aria-hidden="true">
    <defs><clipPath id="cover-left"><rect x="0" y="0" width="378" height="534"/></clipPath></defs>
    <rect x="0" y="0" width="62" height="26" fill="var(--teal)"/>
    <path clip-path="url(#cover-left)" d="M296 0 A118 118 0 0 1 296 236 L296 176 A58 58 0 0 0 296 60 Z" fill="var(--teal)"/>
    <path d="M125 267 A193 193 0 0 1 318 460 L230 460 A105 105 0 0 0 125 355 Z" fill="var(--blue-soft)" opacity=".82"/>
    <path d="M757 208 A192 192 0 0 0 565 400 L660 400 A97 97 0 0 1 757 303 Z" fill="var(--teal)" opacity=".92"/>
  </svg>

  <div class="abs contact" style="top:443px">
    <svg viewBox="0 0 10 10"><path d="M2 0.5 L3.8 2.4 L2.9 3.6 Q4 5.9 6.4 7.1 L7.6 6.2 L9.5 8 L8.4 9.5 Q3.5 9.2 0.5 1.6 Z" fill="var(--ink)"/></svg>
    <span>05550 18243</span>
  </div>
  <div class="abs contact" style="top:460px">
    <svg viewBox="0 0 10 10"><rect x="0.5" y="2" width="9" height="6.5" fill="var(--ink)"/><path d="M0.5 2 L5 5.5 L9.5 2" stroke="#fff" stroke-width=".9" fill="none"/></svg>
    <span>care@orvalismed.com</span>
  </div>
  <div class="abs web-bar">
    <svg viewBox="0 0 10 10" width="9" height="9"><circle cx="5" cy="5" r="4.3" fill="none" stroke="#fff" stroke-width=".9"/><ellipse cx="5" cy="5" rx="1.9" ry="4.3" fill="none" stroke="#fff" stroke-width=".8"/><path d="M0.7 5 H9.3" stroke="#fff" stroke-width=".8"/></svg>
    <span>www.orvalismed.com</span>
  </div>

  <div class="abs brand">
    <div class="brand__name"><span class="brand__mark"></span>Orvalis Med</div>
    <div class="brand__tag">Health Care Diagnostic</div>
  </div>

  <h1 class="abs headline">
    WHY SHOULD<br>
    YOU SEND<br>
    <span class="accent">YOUR PATIENT</span><br>
    <span class="strong">ANYWHERE ELSE?</span>
  </h1>
</section>

<section class="spread spread--inside">
  <div class="photo photo--ct" role="img" aria-label="Cardiac CT scanner with patient table"></div>
  <div class="photo photo--xray" role="img" aria-label="Digital X-ray system with detector stand and table"></div>

  <svg class="shapes" viewBox="0 0 757 534" aria-hidden="true">
    <defs><clipPath id="inside-mid"><rect x="0" y="0" width="604" height="534"/></clipPath></defs>
    <rect x="27" y="0" width="57" height="55" fill="var(--blue)"/>
    <path d="M220 17 A154 154 0 0 1 374 171 L300 171 A80 80 0 0 0 220 91 Z" fill="var(--blue-soft)" opacity=".8"/>
    <rect x="266" y="217" width="123" height="52" fill="var(--teal)"/>
    <path clip-path="url(#inside-mid)" d="M439 547 A165 165 0 0 1 604 382 L604 452 A95 95 0 0 0 509 547 Z" fill="var(--blue-soft)" opacity=".85"/>
    <rect x="357" y="470" width="247" height="44" fill="var(--teal)" opacity=".92"/>
  </svg>

  <div class="abs info-panel">
    <svg class="shapes" viewBox="0 0 368 194" style="width:368px;height:194px" aria-hidden="true">
      <path d="M252 0 H368 V170 A116 116 0 0 0 252 0 Z" fill="var(--teal)" opacity=".85"/>
      <path d="M250 10 A110 110 0 0 1 360 120 L320 120 A70 70 0 0 0 250 50 Z" fill="var(--blue-soft)"/>
    </svg>
    <h2>WHY CHOOSE OUR CARDIOLOGY?</h2>
    <p class="body-copy">Your heart is at the centre of everything we do. Orvalis Med brings cardiologists, radiologists and technicians together in one place, so every cardiac exam is planned, performed and reported by a dedicated team. Cardiac MRI shows the structure and function of the heart muscle without radiation, while coronary CT angiography maps the arteries in a few seconds. Echocardiography and Doppler ultrasound follow valves and blood flow in real time, and stress tests reveal how the heart responds to effort. Results are read by specialists and sent to you and your doctor quickly, with clear reports and images to keep. Early, accurate diagnosis means earlier treatment and more healthy years for every patient who trusts us with their heart.</p>
  </div>

  <div class="abs story-box">
    <svg class="shapes" viewBox="0 0 310 236" style="width:310px;height:236px" aria-hidden="true">
      <circle cx="110" cy="290" r="128" fill="var(--teal)"/>
      <circle cx="118" cy="296" r="100" fill="var(--paper)"/>
    </svg>
    <p class="body-copy">Beyond the heart, our centre looks after the whole body. MRI studies the brain, spine, knees and joints in fine detail, CT gives rapid answers for chest, abdomen and trauma, and digital X-ray checks bones and lungs with a very low dose. Ultrasound follows organs, vessels and legs without radiation. Every exam is booked quickly, performed on modern equipment by a caring team and reported by specialists who share results with your doctor, so you receive one clear answer in a calm, welcoming setting close to home.</p>
  </div>

  <ul class="abs bullets">
    <li class="wide">Cardiac MRI to study the heart muscle, chambers and function without radiation.</li>
    <li class="wide">Coronary CT angiography for a fast and detailed view of the heart arteries.</li>
    <li class="wide">Echocardiography and Doppler ultrasound of valves and blood flow in real time.</li>
    <li class="wide">ECG, Holter monitoring and stress tests read by experienced cardiologists.</li>
    <li class="narrow">Brain and spine MRI for headaches, nerves and back pain.</li>
    <li class="narrow">Knee, leg and joint imaging for sport and injuries.</li>
    <li class="narrow">Digital X-ray and ultrasound with low dose and quick results.</li>
  </ul>
</section>

</body>
</html>
```